I need a box design created for a DNA Fitness Test

I need a modern and sleek box design for a fitness test. The box needs to have our logo on it and should be clean and modern. The Box is 9 Inches Long 3 and 3/4 inches wide, and 2 inches tall. Company logo attached. The company name is cedar vitality.

Target Market(s)

Fitness

Industry/Entity Type

Fitness

Requirements
Must have
• Our logo

```html
<!DOCTYPE html>
<html lang="en">
<head>
<meta charset="utf-8">
<title>Cedar Vitality – DNA Fitness Test Box Wrap</title>
<link href="https://fonts.googleapis.com/css2?family=Montserrat:wght@700&family=Open+Sans:wght@700&display=swap" rel="stylesheet">
<style>
  :root {
    --page: #f4f5f7;
    --navy: #0a2150;
    --navy-deep: #071a42;
    --water-dark: #1560b0;
    --water-mid: #1f7fd0;
    --water-light: #33a4e6;
    --panel-glow: #1a5aa8;
    --green: #86b526;
    --white: #ffffff;
  }
  * { box-sizing: border-box; margin: 0; padding: 0; }
  html, body {
    width: 1189px; height: 1200px; overflow: hidden;
    background: var(--page);
  }
  .canvas {
    position: relative;
    width: 1189px; height: 1200px;
  }
  .box-wrap {
    position: absolute;
    left: 0; top: 336px;
    width: 1189px; height: 527px;
    overflow: hidden;
    background: var(--navy-deep);
  }
  .water-surface {
    position: absolute; inset: 0;
  }
  .end-curves {
    position: absolute; inset: 0;
  }
  .brand-panel {
    position: absolute;
    left: 461px; top: 0;
    width: 327px; height: 350px;
    background: radial-gradient(ellipse at 50% 35%, var(--panel-glow) 0%, var(--navy) 62%, var(--navy-deep) 100%);
  }
  .brand-mark {
    position: absolute;
    left: 50%; top: 42px;
    width: 92px; height: 92px;
    margin-left: -46px;
    border-radius: 50%;
    background: var(--green);
  }
  .brand-name {
    position: absolute;
    left: 0; right: 0; top: 170px;
    text-align: center;
    font-family: "Montserrat", sans-serif;
    font-weight: 700;
    font-size: 38px;
    line-height: 1.08;
    letter-spacing: 1px;
    color: var(--white);
  }
  .product-band {
    position: absolute;
    left: 0; right: 0; bottom: 0;
    height: 46px;
    background: var(--green);
    display: flex; align-items: center; justify-content: center;
    font-family: "Open Sans", sans-serif;
    font-weight: 700;
    font-size: 26px;
    color: var(--white);
  }
</style>
</head>
<body>
  <div class="canvas">
    <section class="box-wrap">
      <svg class="water-surface" width="1189" height="527" viewBox="0 0 1189 527" role="img" aria-label="Photograph of water droplets on a blue surface">
        <defs>
          <linearGradient id="waterTone" x1="0" y1="0" x2="1" y2="0.4">
            <stop offset="0" stop-color="var(--water-mid)"/>
            <stop offset="0.45" stop-color="var(--water-dark)"/>
            <stop offset="0.8" stop-color="var(--water-mid)"/>
            <stop offset="1" stop-color="var(--water-light)"/>
          </linearGradient>
        </defs>
        <rect width="1189" height="527" fill="url(#waterTone)"/>
      </svg>
      <svg class="end-curves" width="1189" height="527" viewBox="0 0 1189 527" aria-hidden="true">
        <path d="M0 0 H14 Q120 263 14 527 H0 Z" fill="var(--navy-deep)"/>
        <path d="M1189 0 H1175 Q1069 263 1175 527 H1189 Z" fill="var(--navy-deep)"/>
      </svg>
      <div class="brand-panel">
        <span class="brand-mark"></span>
        <p class="brand-name">CEDAR<br>VITALITY</p>
        <p class="product-band">DNA Fitness Test</p>
      </div>
    </section>
  </div>
</body>
</html>
```